Verdalunex webpage design

We are offering eco/sustainable theme vacations and make them bookable via our site. Our reference site is www.voyelmora.com. We want something similar but with a bit more creativity and elegant design. In our colors, which would depend on our logo colors.

NB: WE ARE NOT ASKING FOR A FULL BLOWN SITE. WE NEED 2 PAGE DESIGN FOR THE FIRST IMPRESSION. AFTER THAT WE CREATE A BUDGET FOR COMPLETION OF THE PROJECT.

Target Market(s)

Eco/Sustainable tourism.

Industry/Entity Type

Tourism

Coding

Coded - Design and coding required

Number of Pages Required

2 page

Requirements
Must have
• Reference site is voyelmora.com. But be creative and design something a bit different and more beautiful.
• NB: WE ARE NOT ASKING FOR A FULL BLOWN SITE. WE NEED 2 PAGE DESIGN FOR THE FIRST IMPRESSION. AFTER THAT WE CREATE A BUDGET FOR COMPLETION OF THE PROJECT.
• Please see our logo.

```html
<!DOCTYPE html>
<html lang="en">
<head>
<meta charset="utf-8">
<title>Verdalunex – Memorable Travel Experience</title>
<link href="https://fonts.googleapis.com/css2?family=Montserrat:wght@300;400;500;600;700;800&family=Open+Sans:wght@400;600;700&display=swap" rel="stylesheet">
<style>
:root{
  --mint:#86dcc0;
  --mint-dark:#5fc6a6;
  --ink:#2d2d2d;
  --ink-soft:#555;
  --bar:#2f2f2f;
  --page:#f2f3f7;
  --white:#fff;
  --star:#f5b820;
  --footer:#1d1d1d;
  --line:#e3e3e3;
}
*{box-sizing:border-box;margin:0;padding:0}
html,body{width:1200px;height:4865px;overflow:hidden;background:var(--white)}
body{font-family:"Open Sans",Arial,sans-serif;color:var(--ink);position:relative}
.abs{position:absolute}

/* Hero */
.hero{left:0;top:0;width:1200px;height:616px;background:linear-gradient(180deg,#2a6f9a 0%,#3f8fb9 30%,#a8c7d6 58%,#e9eef0 72%,#cdd8dc 100%);overflow:hidden}
.hero-photo{position:absolute;inset:0;background:radial-gradient(ellipse at 75% 85%,#ffffff 0%,rgba(255,255,255,0) 40%),radial-gradient(ellipse at 20% 90%,#f4f6f6 0%,rgba(255,255,255,0) 35%)}
.nav{position:absolute;left:0;top:0;width:1200px;height:170px}
.brand{position:absolute;left:42px;top:58px;display:flex;align-items:center;gap:10px;font-family:"Montserrat",sans-serif;font-weight:300;font-size:54px;color:var(--white);letter-spacing:-1px}
.brand-dot{width:20px;height:20px;border-radius:50%;background:var(--mint)}
.nav-links{position:absolute;right:42px;top:70px;display:flex;align-items:center;gap:42px;font-family:"Montserrat",sans-serif;font-size:17px;color:var(--white);font-weight:500}
.btn-signup{background:var(--mint);padding:7px 16px;border-radius:4px}
.hero-title{position:absolute;left:0;width:1200px;top:244px;text-align:center;font-family:"Montserrat",sans-serif;font-weight:700;font-size:52px;color:var(--white);text-shadow:0 2px 8px rgba(0,0,0,.35)}
.hero-sub{position:absolute;left:0;width:1200px;top:318px;text-align:center;font-family:"Montserrat",sans-serif;font-weight:600;font-size:24px;color:var(--white);text-shadow:0 2px 6px rgba(0,0,0,.35)}
.search{position:absolute;left:113px;top:366px;width:973px;height:78px;background:var(--white);border-radius:6px;display:flex;overflow:hidden;box-shadow:0 4px 16px rgba(0,0,0,.2)}
.search-field{flex:1;display:flex;align-items:center;gap:14px;padding-left:22px;border-right:1px solid var(--line)}
.search-field svg{flex:none}
.search-label{font-family:"Montserrat",sans-serif;font-weight:700;font-size:12px;text-transform:uppercase;color:var(--ink)}
.search-value{font-size:19px;color:var(--ink-soft)}
.search-go{width:86px;background:var(--mint);display:flex;align-items:center;justify-content:center}

/* Stats */
.stats{left:0;top:616px;width:1200px;height:162px;background:#1f1f1f;display:flex;justify-content:center;gap:70px;align-items:center}
.stat{display:flex;align-items:center;gap:18px;color:var(--white)}
.stat-num{font-family:"Montserrat",sans-serif;font-weight:800;font-size:46px;line-height:1}
.stat-cap{font-family:"Montserrat",sans-serif;font-size:17px;color:var(--mint);font-weight:600}

/* Main listing */
.listing{left:0;top:778px;width:1200px;height:2416px;background:var(--page)}
.filter{position:absolute;left:65px;width:373px;background:var(--white);box-shadow:0 2px 8px rgba(0,0,0,.08)}
.filter-head{height:58px;background:var(--mint);display:flex;align-items:center;gap:14px;padding-left:22px;font-family:"Montserrat",sans-serif;font-weight:700;font-size:18px;color:var(--white)}
.filter-body{padding:16px 30px 10px}
.select{height:44px;border-bottom:1px solid var(--line);display:flex;align-items:center;justify-content:space-between;font-size:16px;color:var(--ink);margin-bottom:14px}
.select.compact{height:40px;margin-bottom:17px}
.caret{width:0;height:0;border-left:9px solid transparent;border-right:9px solid transparent;border-top:10px solid var(--ink)}
.check{display:flex;align-items:center;gap:12px;font-size:16px;margin-bottom:13px}
.box{width:17px;height:17px;border:1.5px solid #777;border-radius:50%}
.show-more{color:#3a8fd0;font-size:15px;font-weight:600;padding-left:29px}
.sort{position:absolute;left:480px;top:90px;font-family:"Montserrat",sans-serif;font-size:17px;font-weight:500;display:flex;gap:10px;align-items:center}
.sort .caret{border-width:7px 6px 0}

.tour{position:absolute;left:477px;width:658px;height:405px;background:var(--white);box-shadow:0 2px 8px rgba(0,0,0,.08);overflow:hidden}
.tour-head{height:65px;background:var(--bar);color:var(--white);font-family:"Montserrat",sans-serif;font-weight:700;font-size:18px;display:flex;align-items:center;justify-content:space-between;padding:0 22px;line-height:1.3}
.tour-head svg{flex:none}
.tour-img{position:absolute;left:26px;top:91px;width:201px;height:207px}
.tour-info{position:absolute;left:265px;top:95px}
.stars{display:flex;gap:3px;align-items:center;font-size:15px;color:var(--ink-soft)}
.from{font-size:24px;margin-top:12px;line-height:1}
.price{font-family:"Montserrat",sans-serif;font-size:44px;font-weight:500;line-height:1.1}
.meta{display:flex;align-items:center;gap:12px;font-size:17px;margin-top:8px}
.tour-feats{position:absolute;left:26px;top:322px;display:flex;gap:26px}
.feat{display:flex;align-items:center;gap:10px;font-size:14px;line-height:1.2;width:150px}
.feat-ico{width:30px;height:30px;border:1.5px solid #777;border-radius:50%;flex:none;display:flex;align-items:center;justify-content:center}
.see{position:absolute;right:0;bottom:0;width:190px;height:125px;background:var(--mint);clip-path:polygon(48% 0,100% 0,100% 100%,0 100%);display:flex;align-items:flex-end;justify-content:flex-end;padding:0 22px 42px 0;font-family:"Montserrat",sans-serif;font-weight:700;font-size:18px;color:var(--white)}
.load{position:absolute;left:697px;top:2296px;width:221px;height:46px;background:#a7a7a7;border-radius:4px;display:flex;align-items:center;justify-content:center;gap:10px;color:var(--white);font-family:"Montserrat",sans-serif;font-weight:600;font-size:17px}

/* Discover */
.discover{left:0;top:3194px;width:1200px;height:730px;background:var(--white)}
.discover h2{position:absolute;left:0;top:72px;width:1200px;text-align:center;font-family:"Montserrat",sans-serif;font-weight:700;font-size:34px;line-height:1.4;color:var(--ink)}
.discover h2 em{font-style:normal;color:var(--mint-dark)}
.world{position:absolute;left:146px;top:179px;width:924px;height:470px;border-radius:20px;background:radial-gradient(ellipse at 30% 40%,#b8c3cc 0%,#cfd6dc 30%,rgba(255,255,255,0) 62%),radial-gradient(ellipse at 70% 45%,#b8c3cc 0%,#d4dade 32%,rgba(255,255,255,0) 64%)}

/* Reviews */
.reviews{left:0;top:3924px;width:1200px;height:448px;background:#f1f1f1}
.reviews h3{position:absolute;left:0;top:56px;width:1200px;text-align:center;font-family:"Montserrat",sans-serif;font-weight:700;font-size:30px}
.rated{position:absolute;left:0;top:118px;width:1200px;text-align:center;font-size:17px;color:var(--ink-soft)}
.review{position:absolute;top:175px;width:420px}
.avatar{position:absolute;left:0;top:0;width:88px;height:88px;border-radius:50%;background:linear-gradient(135deg,#e8d6c8,#c9a68c)}
.review-meta{position:absolute;left:110px;top:6px;font-size:13px;color:var(--ink-soft);display:flex;gap:14px;align-items:center}
.review-title{position:absolute;left:110px;top:34px;font-family:"Montserrat",sans-serif;font-weight:700;font-size:19px}
.review-text{position:absolute;left:110px;top:68px;width:300px;font-size:13px;line-height:1.5;color:var(--ink-soft)}
.review-name{position:absolute;left:110px;top:200px;font-size:14px;font-weight:700;line-height:1.5}
.review-name span{display:block;font-weight:600}
.arrow{position:absolute;top:232px}

/* Footer */
.footer{left:0;top:4372px;width:1200px;height:454px;background:radial-gradient(ellipse at 50% 20%,#2e2e2e,#151515 75%)}
.footer .brand{left:0;width:1200px;justify-content:center;top:82px;font-size:50px}
.fcol{position:absolute;top:196px;color:#cfcfcf;font-size:13px;line-height:1.75}
.fcol h4{font-family:"Montserrat",sans-serif;font-size:13px;font-weight:700;color:var(--mint);letter-spacing:.5px;margin-bottom:6px;padding-bottom:8px;border-bottom:1px solid #444}
.frow{display:flex;align-items:center;gap:10px;margin-bottom:10px}
.ring{width:20px;height:20px;border:1.5px solid var(--mint);border-radius:50%;flex:none}
.social-dot{width:22px;height:22px;border-radius:50%;background:var(--mint);flex:none}
.copyright{left:0;top:4826px;width:1200px;height:39px;display:flex;align-items:center;justify-content:center;font-family:"Montserrat",sans-serif;font-size:11px;font-weight:600;color:var(--ink)}
</style>
</head>
<body>

<header class="abs hero">
  <div class="hero-photo" role="img" aria-label="Whitewashed cliffside village with a pool above a deep blue sea"></div>
  <nav class="nav">
    <div class="brand"><span>Verdalunex</span><span class="brand-dot"></span></div>
    <div class="nav-links">
      <span>US$</span>
      <span>♡ Favorites (0)</span>
      <span>Partners</span>
      <span>Log In</span>
      <span class="btn-signup">Sign Up</span>
    </div>
  </nav>
  <h1 class="hero-title">Memorable Travel Experience</h1>
  <p class="hero-sub">Unique holidays, organized by passionate experts</p>
  <form class="search">
    <div class="search-field">
      <svg width="28" height="34" viewBox="0 0 28 34"><path d="M14 2a11 11 0 0 1 11 11c0 8-11 19-11 19S3 21 3 13A11 11 0 0 1 14 2z" fill="none" stroke="#5fc6a6" stroke-width="2.5"/><circle cx="14" cy="13" r="4" fill="#5fc6a6"/></svg>
      <div><div class="search-label">Destination</div><div class="search-value">Any Destination</div></div>
    </div>
    <div class="search-field">
      <svg width="32" height="32" viewBox="0 0 32 32"><rect x="3" y="6" width="26" height="23" rx="2" fill="none" stroke="#5fc6a6" stroke-width="2.5"/><path d="M3 13h26M10 3v6M22 3v6" stroke="#5fc6a6" stroke-width="2.5"/></svg>
      <div><div class="search-label">Duration and Arrival</div><div class="search-value">Select Date</div></div>
    </div>
    <div class="search-field">
      <svg width="32" height="32" viewBox="0 0 32 32"><path d="M16 3l4 9 9 1-7 6 2 9-8-5-8 5 2-9-7-6 9-1z" fill="none" stroke="#5fc6a6" stroke-width="2.3" stroke-linejoin="round"/></svg>
      <div><div class="search-label">Activity Type</div><div class="search-value">Any Category</div></div>
    </div>
    <div class="search-go"><svg width="36" height="36" viewBox="0 0 36 36"><circle cx="15" cy="15" r="10" fill="none" stroke="#fff" stroke-width="3.5"/><path d="M22 22l10 10" stroke="#fff" stroke-width="3.5" stroke-linecap="round"/></svg></div>
  </form>
</header>

<section class="abs stats">
  <div class="stat">
    <svg width="64" height="64" viewBox="0 0 64 64"><circle cx="32" cy="32" r="28" fill="none" stroke="#86dcc0" stroke-width="2.5"/><circle cx="32" cy="26" r="7" fill="none" stroke="#86dcc0" stroke-width="2.5"/><path d="M20 46c2-8 22-8 24 0" fill="none" stroke="#86dcc0" stroke-width="2.5"/></svg>
    <div><div class="stat-num">300+</div><div class="stat-cap">Verdalunexers</div></div>
  </div>
  <div class="stat">
    <svg width="64" height="64" viewBox="0 0 64 64"><rect x="10" y="14" width="44" height="36" rx="4" fill="none" stroke="#86dcc0" stroke-width="2.5" transform="rotate(-15 32 32)"/><path d="M18 30h26M18 38h18" stroke="#86dcc0" stroke-width="2.5" transform="rotate(-15 32 32)"/></svg>
    <div><div class="stat-num">15,000+</div><div class="stat-cap">Travel Packages</div></div>
  </div>
  <div class="stat">
    <svg width="64" height="64" viewBox="0 0 64 64"><circle cx="22" cy="24" r="7" fill="none" stroke="#86dcc0" stroke-width="2.5"/><circle cx="42" cy="24" r="7" fill="none" stroke="#86dcc0" stroke-width="2.5"/><path d="M8 48c2-10 26-10 28 0M28 48c2-10 26-10 28 0" fill="none" stroke="#86dcc0" stroke-width="2.5"/></svg>
    <div><div class="stat-num">500,000+</div><div class="stat-cap">Customers per Month</div></div>
  </div>
</section>

<main class="abs listing">
  <aside>
    <div class="filter" style="top:78px">
      <div class="filter-head"><svg width="22" height="22" viewBox="0 0 22 22"><circle cx="11" cy="11" r="9" fill="none" stroke="#fff" stroke-width="2"/><path d="M2 11h18M11 2c4 5 4 13 0 18M11 2c-4 5-4 13 0 18" fill="none" stroke="#fff" stroke-width="1.5"/></svg>Destinations</div>
      <div class="filter-body">
        <div class="select compact">Europe<span class="caret"></span></div>
        <div class="select compact">Asia &amp; Oceania<span class="caret"></span></div>
        <div class="select compact">Africa &amp; Middle East<span class="caret"></span></div>
        <div class="select compact">The Americas &amp; Caribbean<span class="caret"></span></div>
      </div>
    </div>

    <div class="filter" style="top:415px">
      <div class="filter-head"><svg width="22" height="22" viewBox="0 0 22 22"><rect x="2" y="4" width="18" height="16" rx="2" fill="none" stroke="#fff" stroke-width="2"/><path d="M2 9h18" stroke="#fff" stroke-width="2"/></svg>Arrival Date</div>
      <div class="filter-body">
        <div class="check"><span class="box"></span>2019 May (10234)</div>
        <div class="check"><span class="box"></span>2019 June (11560)</div>
        <div class="check"><span class="box"></span>2019 July (10610)</div>
        <div class="check"><span class="box"></span>2019 August (10325)</div>
        <div class="check"><span class="box"></span>2019 September (10626)</div>
        <div class="show-more">show more</div>
      </div>
    </div>

    <div class="filter" style="top:740px">
      <div class="filter-head"><svg width="22" height="22" viewBox="0 0 22 22"><circle cx="11" cy="11" r="9" fill="none" stroke="#fff" stroke-width="2"/><path d="M11 5v6l4 3" fill="none" stroke="#fff" stroke-width="2"/></svg>Duration</div>
      <div class="filter-body">
        <div class="check"><span class="box"></span>2 days (792)</div>
        <div class="check"><span class="box"></span>From 3 to 7 days (8599)</div>
        <div class="check"><span class="box"></span>From 1 to 2 weeks (7106)</div>
        <div class="check"><span class="box"></span>More than 2 weeks (1890)</div>
      </div>
    </div>

    <div class="filter" style="top:989px">
      <div class="filter-head"><svg width="22" height="22" viewBox="0 0 22 22"><path d="M2 13l18-7-4 11-5-3-3 4z" fill="none" stroke="#fff" stroke-width="2" stroke-linejoin="round"/></svg>Airport Transfer</div>
      <div class="filter-body">
        <div class="check"><span class="box"></span>Airport transfer included (5153)</div>
        <div class="check"><span class="box"></span>Airport transfer available (2793)</div>
      </div>
    </div>

    <div class="filter" style="top:1171px">
      <div class="filter-head"><svg width="22" height="22" viewBox="0 0 22 22"><rect x="2" y="2" width="8" height="8" fill="none" stroke="#fff" stroke-width="2"/><rect x="12" y="2" width="8" height="8" fill="none" stroke="#fff" stroke-width="2"/><rect x="2" y="12" width="8" height="8" fill="none" stroke="#fff" stroke-width="2"/><rect x="12" y="12" width="8" height="8" fill="none" stroke="#fff" stroke-width="2"/></svg>Categories</div>
      <div class="filter-body">
        <div class="select">Accomodation Type<span class="caret"></span></div>
        <div class="select">Activity<span class="caret"></span></div>
        <div class="select">Audience<span class="caret"></span></div>
        <div class="select">Budget<span class="caret"></span></div>
        <div class="select">Duration<span class="caret"></span></div>
        <div class="select">Experience Level<span class="caret"></span></div>
        <div class="select">Experience Type<span class="caret"></span></div>
        <div class="select">Focus/Atmosphere<span class="caret"></span></div>
        <div class="select">Food<span class="caret"></span></div>
        <div class="select">Intensity Level<span class="caret"></span></div>
        <div class="select">Location<span class="caret"></span></div>
        <div class="select">Special Occasion<span class="caret"></span></div>
        <div class="select">Time Periods<span class="caret"></span></div>
      </div>
    </div>

    <div class="filter" style="top:2034px">
      <div class="filter-head"><svg width="22" height="22" viewBox="0 0 22 22"><circle cx="11" cy="11" r="9" fill="none" stroke="#fff" stroke-width="2"/><path d="M14 7h-4a2 2 0 0 0 0 4h2a2 2 0 0 1 0 4H8M11 5v12" fill="none" stroke="#fff" stroke-width="1.6"/></svg>Price per Trip</div>
      <div class="filter-body">
        <div class="check"><span class="box"></span>From US$0 to US$112 (299)</div>
        <div class="check"><span class="box"></span>From US$112 to US$337 (1448)</div>
        <div class="check"><span class="box"></span>From US$337 to US$1,011 (6598)</div>
        <div class="check"><span class="box"></span>More than US$1,011 (8397)</div>
      </div>
    </div>
  </aside>

  <div class="sort">Sort by : Recommended <span class="caret"></span></div>

  <article class="tour" style="top:130px">
    <div class="tour-head">5 Days Italy by Train Tour in Rome, Florence, Venice<svg width="26" height="24" viewBox="0 0 26 24"><path d="M13 22S2 15 2 8a5.5 5.5 0 0 1 11-1 5.5 5.5 0 0 1 11 1c0 7-11 14-11 14z" fill="none" stroke="#fff" stroke-width="2.2"/></svg></div>
    <div class="tour-img" role="img" aria-label="Ancient Roman amphitheatre under a blue sky" style="background:linear-gradient(180deg,#6fa9d8 0%,#9cc3e0 40%,#c9a276 60%,#8c6a45 100%)"></div>
    <div class="tour-info">
      <div class="stars"><span style="color:var(--star);font-size:20px;letter-spacing:1px">★★★★★</span>&nbsp;(3)</div>
      <div class="from">from</div><div class="price">US$1,145</div>
      <div class="meta"><svg width="16" height="20" viewBox="0 0 16 20"><circle cx="8" cy="5" r="4" fill="#5fc6a6"/><path d="M1 19c0-8 14-8 14 0z" fill="#5fc6a6"/></svg>1 person</div>
      <div class="meta"><svg width="16" height="16" viewBox="0 0 16 16"><rect x="1" y="2" width="14" height="13" fill="#5fc6a6"/></svg>13 days / 12 nights</div>
    </div>
    <div class="tour-feats">
      <div class="feat"><span class="feat-ico">✕</span>Flexible cancellation policy</div>
      <div class="feat"><span class="feat-ico">✈</span>Airport transfer included</div>
      <div class="feat"><span class="feat-ico">✓</span>All meals included</div>
    </div>
    <div class="see">See Details</div>
  </article>

  <article class="tour" style="top:561px">
    <div class="tour-head">8 Days Northern Spain Guided Tour in Province of León<svg width="26" height="24" viewBox="0 0 26 24"><path d="M13 22S2 15 2 8a5.5 5.5 0 0 1 11-1 5.5 5.5 0 0 1 11 1c0 7-11 14-11 14z" fill="none" stroke="#fff" stroke-width="2.2"/></svg></div>
    <div class="tour-img" role="img" aria-label="Old Spanish city at golden sunset" style="background:linear-gradient(180deg,#f2c48a 0%,#e59a55 45%,#a4683e 75%,#5b3f2b 100%)"></div>
    <div class="tour-info">
      <div class="stars"><span style="color:var(--star);font-size:20px;letter-spacing:1px">★★★★★</span>&nbsp;(3)</div>
      <div class="from">from</div><div class="price">US$1,145</div>
      <div class="meta"><svg width="16" height="20" viewBox="0 0 16 20"><circle cx="8" cy="5" r="4" fill="#5fc6a6"/><path d="M1 19c0-8 14-8 14 0z" fill="#5fc6a6"/></svg>1 person</div>
      <div class="meta"><svg width="16" height="16" viewBox="0 0 16 16"><rect x="1" y="2" width="14" height="13" fill="#5fc6a6"/></svg>13 days / 12 nights</div>
    </div>
    <div class="tour-feats">
      <div class="feat"><span class="feat-ico">✕</span>Flexible cancellation policy</div>
      <div class="feat"><span class="feat-ico">✈</span>Airport transfer included</div>
      <div class="feat"><span class="feat-ico">✓</span>All meals included</div>
    </div>
    <div class="see">See Details</div>
  </article>

  <article class="tour" style="top:989px">
    <div class="tour-head"><span>4 Days Luxury Tour of Madrid, Burgos, and<br>La Rioja in Spain</span><svg width="26" height="24" viewBox="0 0 26 24"><path d="M13 22S2 15 2 8a5.5 5.5 0 0 1 11-1 5.5 5.5 0 0 1 11 1c0 7-11 14-11 14z" fill="none" stroke="#fff" stroke-width="2.2"/></svg></div>
    <div class="tour-img" role="img" aria-label="City skyline seen from a hilltop park" style="background:linear-gradient(180deg,#8fbde8 0%,#c6dcef 45%,#8a9a6a 70%,#4d6a3a 100%)"></div>
    <div class="tour-info">
      <div class="stars"><span style="color:var(--star);font-size:20px;letter-spacing:1px">★★★★★</span>&nbsp;(3)</div>
      <div class="from">from</div><div class="price">US$1,145</div>
      <div class="meta"><svg width="16" height="20" viewBox="0 0 16 20"><circle cx="8" cy="5" r="4" fill="#5fc6a6"/><path d="M1 19c0-8 14-8 14 0z" fill="#5fc6a6"/></svg>1 person</div>
      <div class="meta"><svg width="16" height="16" viewBox="0 0 16 16"><rect x="1" y="2" width="14" height="13" fill="#5fc6a6"/></svg>13 days / 12 nights</div>
    </div>
    <div class="tour-feats">
      <div class="feat"><span class="feat-ico">✕</span>Flexible cancellation policy</div>
      <div class="feat"><span class="feat-ico">✈</span>Airport transfer included</div>
      <div class="feat"><span class="feat-ico">✓</span>All meals included</div>
    </div>
    <div class="see">See Details</div>
  </article>

  <article class="tour" style="top:1421px">
    <div class="tour-head">10 Days Guided Sightseeing Tour of Vietnam<svg width="26" height="24" viewBox="0 0 26 24"><path d="M13 22S2 15 2 8a5.5 5.5 0 0 1 11-1 5.5 5.5 0 0 1 11 1c0 7-11 14-11 14z" fill="none" stroke="#fff" stroke-width="2.2"/></svg></div>
    <div class="tour-img" role="img" aria-label="Colourful lantern-lined old town street" style="background:linear-gradient(180deg,#e8d07a 0%,#9bbd6a 45%,#6e9a52 70%,#c89a5a 100%)"></div>
    <div class="tour-info">
      <div class="stars"><span style="color:var(--star);font-size:20px;letter-spacing:1px">★★★★★</span>&nbsp;(3)</div>
      <div class="from">from</div><div class="price">US$1,145</div>
      <div class="meta"><svg width="16" height="20" viewBox="0 0 16 20"><circle cx="8" cy="5" r="4" fill="#5fc6a6"/><path d="M1 19c0-8 14-8 14 0z" fill="#5fc6a6"/></svg>1 person</div>
      <div class="meta"><svg width="16" height="16" viewBox="0 0 16 16"><rect x="1" y="2" width="14" height="13" fill="#5fc6a6"/></svg>13 days / 12 nights</div>
    </div>
    <div class="tour-feats">
      <div class="feat"><span class="feat-ico">✕</span>Flexible cancellation policy</div>
      <div class="feat"><span class="feat-ico">✈</span>Airport transfer included</div>
      <div class="feat"><span class="feat-ico">✓</span>All meals included</div>
    </div>
    <div class="see">See Details</div>
  </article>

  <article class="tour" style="top:1852px">
    <div class="tour-head">8 Days Japan<svg width="26" height="24" viewBox="0 0 26 24"><path d="M13 22S2 15 2 8a5.5 5.5 0 0 1 11-1 5.5 5.5 0 0 1 11 1c0 7-11 14-11 14z" fill="none" stroke="#fff" stroke-width="2.2"/></svg></div>
    <div class="tour-img" role="img" aria-label="Castle framed by cherry blossom" style="background:linear-gradient(180deg,#c9dcef 0%,#f1d3dc 45%,#e7b7c6 70%,#8a8f8a 100%)"></div>
    <div class="tour-info">
      <div class="stars"><span style="color:var(--star);font-size:20px;letter-spacing:1px">★★★★★</span>&nbsp;(3)</div>
      <div class="from">from</div><div class="price">US$1,145</div>
      <div class="meta"><svg width="16" height="20" viewBox="0 0 16 20"><circle cx="8" cy="5" r="4" fill="#5fc6a6"/><path d="M1 19c0-8 14-8 14 0z" fill="#5fc6a6"/></svg>1 person</div>
      <div class="meta"><svg width="16" height="16" viewBox="0 0 16 16"><rect x="1" y="2" width="14" height="13" fill="#5fc6a6"/></svg>13 days / 12 nights</div>
    </div>
    <div class="tour-feats">
      <div class="feat"><span class="feat-ico">✕</span>Flexible cancellation policy</div>
      <div class="feat"><span class="feat-ico">✈</span>Airport transfer included</div>
      <div class="feat"><span class="feat-ico">✓</span>All meals included</div>
    </div>
    <div class="see">See Details</div>
  </article>

  <div class="load"><svg width="20" height="20" viewBox="0 0 20 20"><circle cx="10" cy="10" r="8" fill="none" stroke="#fff" stroke-width="2"/><path d="M10 6v8M6 10h8" stroke="#fff" stroke-width="2"/></svg>Load More</div>
</main>

<section class="abs discover">
  <h2>We enable you to easily <em>discover, plan, and book</em> unique<br>travel experiences anywhere in the world</h2>
  <div class="world" role="img" aria-label="Grey world map with circular travel photos pinned on different continents"></div>
</section>

<section class="abs reviews">
  <h3>Reviews from ReviewNest</h3>
  <p class="rated">Rated 8.7 out of 10 (Great) in 424 reviews</p>
  <svg class="arrow" style="left:90px" width="20" height="30" viewBox="0 0 20 30"><path d="M16 3L4 15l12 12" fill="none" stroke="#333" stroke-width="3.5"/></svg>
  <svg class="arrow" style="left:1090px" width="20" height="30" viewBox="0 0 20 30"><path d="M4 3l12 12L4 27" fill="none" stroke="#333" stroke-width="3.5"/></svg>

  <div class="review" style="left:135px">
    <div class="avatar" role="img" aria-label="Reviewer portrait"></div>
    <div class="review-meta"><span style="color:var(--star);font-size:15px">★★★★★</span>Reviewed 2 days ago</div>
    <div class="review-title">Well Organized!</div>
    <p class="review-text">Lorem ipsum dolor sit amet, consectetur adipiscing elit. Duis faucibus ultricies varius. Proin molestie viverra dolor nec fermentum. Vivamus porttitor consectetur volutpat egestas. Curabitur tristique imperdiet ante.</p>
    <div class="review-name">Anna Morello<span>Ancaster, ON</span></div>
  </div>

  <div class="review" style="left:640px">
    <div class="avatar" role="img" aria-label="Reviewer portrait"></div>
    <div class="review-meta"><span style="color:var(--star);font-size:15px">★★★★★</span>Reviewed 2 days ago</div>
    <div class="review-title">Well Organized!</div>
    <p class="review-text">Lorem ipsum dolor sit amet, consectetur adipiscing elit. Duis faucibus ultricies varius. Proin molestie viverra dolor nec fermentum. Vivamus porttitor consectetur volutpat egestas. Curabitur tristique imperdiet ante.</p>
    <div class="review-name">Jenna Garrow<span>Ancaster, ON</span></div>
  </div>
</section>

<footer class="abs footer">
  <div class="brand"><span>Verdalunex</span><span class="brand-dot"></span></div>
  <div class="fcol" style="left:130px;width:190px">
    <h4>QUICK LINKS</h4>
    <div>About Verdalunex</div><div>Add/Manage Your Business</div><div>Become an Affiliate</div><div>Site Map</div><div>Work With Us</div>
  </div>
  <div class="fcol" style="left:390px;width:220px">
    <h4>RECENT BLOG</h4>
    <div>Spring &amp; Blossom Season Traditions</div><div>The Best Ski &amp; Snowboard Festivals</div><div>Europe's Best Christmas Markets</div><div>A Hipster's Guide to London</div><div>A Guide to Authentic Mexican Food</div>
  </div>
  <div class="fcol" style="left:712px;width:200px">
    <h4>CONTACT</h4>
    <div class="frow"><span class="ring"></span><span>Verdalunex<br>48 Canal Row<br>Utrecht, Netherlands</span></div>
    <div class="frow"><span class="ring"></span>1800 555 0199</div>
    <div class="frow"><span class="ring"></span>hello@verdalunex.com</div>
  </div>
  <div class="fcol" style="left:975px;width:110px">
    <h4>FOLLOW US</h4>
    <div class="frow"><span class="social-dot"></span>Friendora</div>
    <div class="frow"><span class="social-dot"></span>Chatterly</div>
    <div class="frow"><span class="social-dot"></span>Pictora</div>
  </div>
</footer>

<div class="abs copyright">COPYRIGHT © 2019 VERDALUNEX. ALL RIGHTS RESERVED.</div>

</body>
</html>
```